Bramwell Business Card Design

hello,
we are looking for a business card design for our Fintech Company. We are credit card processing company that is also expanding in to the crypto market. We will be focusing on crypto processing, with a crypto wallet and crypto exchange. We like the purple in the logo. We want something modern and sophisticated but at the same time simple and trust worthy to work with banks.

Industry/Entity Type

Fintech

Logo Text

Bramwell

```html
<!DOCTYPE html>
<html lang="en">
<head>
<meta charset="utf-8">
<title>Bramwell Business Card</title>
<link href="https://fonts.googleapis.com/css2?family=Montserrat:wght@700&family=Questrial&display=swap" rel="stylesheet">
<style>
  :root {
    --backdrop: #e6e1dc;
    --navy: #1c2f4f;
    --white: #ffffff;
    --violet: #5b3fc4;
  }
  html, body { margin: 0; padding: 0; overflow: hidden; }
  body {
    width: 1200px; height: 1000px;
    background: var(--backdrop);
    position: relative;
    font-family: "Questrial", sans-serif;
    color: var(--navy);
  }
  .card { position: absolute; width: 480px; height: 305px; }
  .card-front { left: 89px; top: 348px; background: var(--navy); }
  .card-back { left: 631px; top: 349px; background: var(--white); }

  .wordmark {
    position: absolute;
    font-family: "Questrial", sans-serif;
    font-weight: 400;
    letter-spacing: 2px;
    line-height: 1;
    white-space: nowrap;
  }
  .wordmark .dot {
    position: absolute; border-radius: 50%;
  }
  .card-front .wordmark { left: 76px; top: 140px; font-size: 52px; color: var(--white); }
  .card-front .wordmark .dot { width: 14px; height: 14px; left: 0; top: -22px; background: var(--white); }
  .card-back .wordmark { left: 224px; top: 50px; font-size: 36px; color: var(--navy); }
  .card-back .wordmark .dot { width: 10px; height: 10px; left: -4px; top: -16px; background: var(--navy); }

  .accent-bar { position: absolute; left: 1px; top: 132px; width: 17px; height: 38px; background: var(--navy); }
  .holder-name {
    position: absolute; left: 32px; top: 129px;
    font-family: "Montserrat", sans-serif; font-weight: 700;
    font-size: 22px; letter-spacing: 0.2px; margin: 0;
  }
  .holder-title {
    position: absolute; left: 32px; top: 160px;
    font-size: 13px; letter-spacing: 3.2px;
  }
  .title-rule { position: absolute; left: 191px; top: 167px; width: 255px; height: 2px; background: var(--navy); }

  .contact-list { position: absolute; left: 32px; top: 203px; margin: 0; padding: 0; list-style: none; }
  .contact-list li { display: flex; align-items: center; height: 23.5px; font-size: 13px; letter-spacing: 1.1px; }
  .contact-list svg { width: 12px; height: 12px; margin-right: 11px; fill: var(--navy); }

  .address { position: absolute; left: 249px; top: 202px; font-size: 13px; letter-spacing: 1.1px; line-height: 23px; font-style: normal; }
</style>
</head>
<body>
  <section class="card card-front">
    <div class="wordmark"><span class="dot"></span>BRAMWELL</div>
  </section>

  <section class="card card-back">
    <div class="wordmark"><span class="dot"></span>BRAMWELL</div>
    <div class="accent-bar"></div>
    <h1 class="holder-name">DANIEL HARTWELL</h1>
    <div class="holder-title">Founder &amp; Ceo</div>
    <div class="title-rule"></div>

    <ul class="contact-list">
      <li>
        <svg viewBox="0 0 24 24" aria-hidden="true"><path d="M6.6 10.8a15.1 15.1 0 0 0 6.6 6.6l2.2-2.2a1 1 0 0 1 1-.25 11.4 11.4 0 0 0 3.6.57 1 1 0 0 1 1 1V20a1 1 0 0 1-1 1A17 17 0 0 1 3 4a1 1 0 0 1 1-1h3.5a1 1 0 0 1 1 1c0 1.25.2 2.45.57 3.57a1 1 0 0 1-.25 1z"/></svg>
        203-555-0147
      </li>
      <li>
        <svg viewBox="0 0 24 24" aria-hidden="true"><path d="M2 5h20v14H2z M2 5l10 7 10-7" /></svg>
        info@bramwell.com
      </li>
      <li>
        <svg viewBox="0 0 24 24" aria-hidden="true"><path d="M12 2a10 10 0 1 0 0 20 10 10 0 0 0 0-20zm6.9 9h-3a15 15 0 0 0-1.3-5.6A8 8 0 0 1 18.9 11zM12 4c.9 1.2 1.8 3.6 2 7h-4c.2-3.4 1.1-5.8 2-7zM9.4 5.4A15 15 0 0 0 8.1 11h-3a8 8 0 0 1 4.3-5.6zM5.1 13h3a15 15 0 0 0 1.3 5.6A8 8 0 0 1 5.1 13zM12 20c-.9-1.2-1.8-3.6-2-7h4c-.2 3.4-1.1 5.8-2 7zm2.6-1.4a15 15 0 0 0 1.3-5.6h3a8 8 0 0 1-4.3 5.6z"/></svg>
        www.bramwell.com
      </li>
    </ul>

    <address class="address">
      1280 Alder Crest Avenue<br>
      Suite 210 Harbor Point<br>
      Road California 90410
    </address>
  </section>
</body>
</html>
```